Banners for a bowtie/tie Fashion shop

I need banners (770x100) for a necktie and bowtie shop (http://www.movelia.dk)

5 BOWTIE BANNERS:

I need the 3 text versions for eatch bowtie banner:

Danmarks største udvalg af butterfly
Køb butterfly. FRI fragt og FRI retur
Butterfly fra 199,- inkl. FRI fragt

5 NECKTIE BANNERS:

I need the 3 text versions for eatch necktie banner:

Danmarks største udvalg af slips
Køb slips. FRI fragt og FRI retur
Slips fra 199,- inkl. FRI fragt

All banners should contain the logo. All in JPG format and Photoshop/Inddesign/illustrator format

Target Market(s)

Guys and Gays

Industry/Entity Type

Shop

Requirements
Must have
• Logo
Nice to have
• Nice new pictures

```html
<!DOCTYPE html>
<html lang="da">
<head>
<meta charset="utf-8">
<title>kavrino – bannere</title>
<link rel="stylesheet" href="https://fonts.googleapis.com/css2?family=Maven+Pro:wght@400;500;600&display=swap">
<style>
  :root {
    --stage: #262626;
    --banner: #ffffff;
    --ink: #2b2b2b;
    --logo-ink: #1c1c1c;
    --muted: #7a7a7a;
    --tag-bg: #9a9a9a;
    --tag-ink: #ffffff;
    --suit-dark: #0f0f10;
    --suit-mid: #2a2a2c;
    --shirt: #ececec;
    --tie: #b8bcc4;
  }
  * { box-sizing: border-box; margin: 0; padding: 0; }
  html, body { width: 986px; height: 1200px; overflow: hidden; }
  body {
    background: var(--stage);
    font-family: "Maven Pro", sans-serif;
    position: relative;
  }
  .banner {
    position: absolute;
    left: 72px;
    width: 844px;
    height: 110px;
    background: var(--banner);
    box-shadow: 0 6px 14px rgba(0,0,0,.55);
    overflow: hidden;
  }
  .logo {
    position: absolute;
    top: 0;
    height: 110px;
    width: 230px;
    display: flex;
    align-items: center;
    justify-content: center;
    font-size: 50px;
    font-weight: 400;
    color: var(--logo-ink);
    letter-spacing: -0.5px;
  }
  .photo { position: absolute; top: 0; height: 110px; }
  .photo--bowtie {
    background: linear-gradient(90deg, var(--suit-dark) 0%, var(--suit-mid) 30%, var(--shirt) 42%, var(--shirt) 58%, var(--suit-mid) 70%, var(--suit-dark) 100%);
  }
  .photo--tie {
    background: linear-gradient(90deg, var(--suit-dark) 0%, var(--suit-mid) 30%, #d9dde4 40%, var(--tie) 50%, #d9dde4 60%, var(--suit-mid) 70%, var(--suit-dark) 100%);
  }
  .copy {
    position: absolute;
    top: 0;
    height: 110px;
    width: 340px;
    display: flex;
    flex-direction: column;
    align-items: center;
    justify-content: center;
    text-align: center;
    color: var(--ink);
    line-height: 1.05;
  }
  .headline { font-size: 36px; font-weight: 600; white-space: nowrap; }
  .headline .light { font-weight: 400; }
  .headline--wide { font-size: 34px; }
  .headline--xl { font-size: 40px; }
  .headline--xxl { font-size: 44px; }
  .statement { font-size: 27px; font-weight: 400; line-height: 1.2; white-space: nowrap; letter-spacing: 0.3px; }
  .statement--bold { font-weight: 600; font-size: 32px; line-height: 1.12; }
  .subline { font-size: 22px; color: var(--muted); letter-spacing: 1px; margin-top: 2px; white-space: nowrap; }
  .subline--spaced { letter-spacing: 2.5px; }
  .tag {
    margin-top: 6px;
    width: 163px;
    background: var(--tag-bg);
    color: var(--tag-ink);
    font-size: 22px;
    letter-spacing: 1.5px;
    line-height: 27px;
  }
</style>
</head>
<body>

  <section class="banner" style="top:91px">
    <div class="logo" style="left:10px">kavrino</div>
    <div class="photo photo--bowtie" style="left:253px;width:272px" role="img" aria-label="Mand i sort smoking med butterfly"></div>
    <div class="copy" style="left:497px">
      <p class="headline">BUTTERFLY</p>
      <p class="headline">FRA 199,- <span class="light">inkl.</span></p>
      <p class="subline">FRI fragt</p>
    </div>
  </section>

  <section class="banner" style="top:253px">
    <div class="logo" style="left:6px">kavrino</div>
    <div class="photo photo--bowtie" style="left:229px;width:271px" role="img" aria-label="Mand i sort smoking med butterfly"></div>
    <div class="copy" style="left:497px">
      <p class="headline headline--xl">KØB BUTTERFLY</p>
      <p class="subline">FRI fragt og FRI retur</p>
    </div>
  </section>

  <section class="banner" style="top:419px">
    <div class="logo" style="left:6px">kavrino</div>
    <div class="photo photo--bowtie" style="left:229px;width:271px" role="img" aria-label="Mand i sort smoking med butterfly"></div>
    <div class="copy" style="left:497px">
      <p class="statement">DANMARKS STØRSTE</p>
      <p class="statement">UDVALG AF BUTTERFLY</p>
    </div>
  </section>

  <section class="banner" style="top:679px">
    <div class="logo" style="left:14px">kavrino</div>
    <div class="photo photo--tie" style="left:245px;width:228px" role="img" aria-label="Mand i mørkt jakkesæt med lysegråt slips"></div>
    <div class="copy" style="left:484px">
      <p class="headline headline--wide">SLIPS FRA 199,- INKL.</p>
      <p class="tag">FRI fragt</p>
    </div>
  </section>

  <section class="banner" style="top:843px">
    <div class="logo" style="left:14px">kavrino</div>
    <div class="photo photo--tie" style="left:245px;width:228px" role="img" aria-label="Mand i mørkt jakkesæt med lysegråt slips"></div>
    <div class="copy" style="left:484px">
      <p class="headline headline--xxl">KØB SLIPS</p>
      <p class="subline subline--spaced">FRI fragt og FRI retur</p>
    </div>
  </section>

  <section class="banner" style="top:1004px">
    <div class="logo" style="left:14px">kavrino</div>
    <div class="photo photo--tie" style="left:245px;width:228px" role="img" aria-label="Mand i mørkt jakkesæt med lysegråt slips"></div>
    <div class="copy" style="left:477px">
      <p class="statement statement--bold">DANMARKS STØRSTE</p>
      <p class="statement statement--bold">UDVALG AF SLIPS</p>
    </div>
  </section>

</body>
</html>
```